100% West Australian Static Banner

I require a static banner to go on a couple of pages in our website (under development) that highlights that we are a 100% Western Australian Owned & Operated company. I would prefer the banner to be in our company colours (blue shades & grey). I also would like it to be eye catching and modern in design. I have included a 100% West Australian rubber stamp logo to be used as well as including our logo so you know our colours. The banner needs to be 1139 x 350 pixels in size.

Target Market(s)

B2B

Requirements
Must have
• Our rubber stamp 100% West Australian logo
• Modern Eye Catching design
• Blue shaded background
Nice to have
• Shading background similar our logo blue colours
• 100% logo can be reversed out if required or colour changed
• Larger text saying - 100% West Australian Owned & Operated

```html
<!DOCTYPE html>
<html lang="en">
<head>
<meta charset="utf-8">
<title>100% West Australian Owned &amp; Operated Banner</title>
<link rel="stylesheet" href="https://fonts.googleapis.com/css2?family=Source+Sans+3:wght@700&display=swap">
<style>
  :root {
    --navy-deep: #121a2b;
    --navy: #18283f;
    --steel-dark: #1d3a55;
    --steel: #24506e;
    --steel-mid: #2b5d80;
    --sky: #5ea6c8;
    --sky-soft: #4f8fb3;
    --white: #ffffff;
  }
  html, body {
    margin: 0;
    padding: 0;
    width: 1200px;
    height: 369px;
    overflow: hidden;
    background: var(--navy-deep);
  }
  .banner {
    position: relative;
    width: 1200px;
    height: 369px;
    overflow: hidden;
    background: var(--navy-deep);
    font-family: "Source Sans 3", Arial, sans-serif;
  }
  .banner__shapes {
    position: absolute;
    inset: 0;
    width: 1200px;
    height: 369px;
    display: block;
  }
  .banner__brand {
    position: absolute;
    left: 52px;
    top: 190px;
    display: flex;
    align-items: center;
    gap: 12px;
    color: var(--sky);
    font-weight: 700;
    font-size: 36px;
    letter-spacing: 0.5px;
  }
  .banner__brand-mark {
    width: 26px;
    height: 26px;
    background: var(--sky);
  }
  .banner__headline {
    position: absolute;
    left: 372px;
    top: 38px;
    margin: 0;
    color: var(--white);
    font-weight: 700;
    font-size: 64px;
    line-height: 80px;
    transform-origin: 0 0;
    transform: rotate(19.5deg);
    white-space: nowrap;
  }
  .banner__headline-line { display: block; }
  .banner__headline-line--second { padding-left: 30px; }
</style>
</head>
<body>
<div class="banner">
  <svg class="banner__shapes" viewBox="0 0 1140 351" preserveAspectRatio="none" aria-hidden="true">
    <defs>
      <linearGradient id="sweep" x1="0" y1="0" x2="1" y2="0">
        <stop offset="0" stop-color="#121a2b" stop-opacity="0"/>
        <stop offset="0.2" stop-color="#8fb4cc" stop-opacity="0.55"/>
        <stop offset="0.45" stop-color="#2b5d80" stop-opacity="0.9"/>
        <stop offset="1" stop-color="#24506e"/>
      </linearGradient>
      <linearGradient id="topright" x1="0" y1="0" x2="0" y2="1">
        <stop offset="0" stop-color="#1b3048"/>
        <stop offset="1" stop-color="#2a5a7c"/>
      </linearGradient>
    </defs>
    <rect width="1140" height="351" fill="var(--navy-deep)"/>
    <polygon points="0,45 120,18 340,95 0,80" fill="var(--steel)"/>
    <polygon points="110,0 600,0 1140,200 1140,230 340,95" fill="var(--steel-dark)"/>
    <polygon points="300,0 620,0 1140,210 720,120" fill="var(--steel)"/>
    <polygon points="600,0 1140,0 1140,200 920,40" fill="url(#topright)"/>
    <polygon points="560,0 730,0 620,32" fill="var(--sky)"/>
    <polygon points="740,0 1140,0 1140,40 920,40" fill="var(--navy)"/>
    <polygon points="760,205 1140,210 1140,290 1010,282" fill="var(--steel-mid)"/>
    <polygon points="150,86 340,95 1140,270 1140,351 720,351 150,105" fill="url(#sweep)"/>
  </svg>

  <div class="banner__brand">
    <span class="banner__brand-mark"></span>
    <span class="banner__brand-name">Coreline</span>
  </div>

  <h1 class="banner__headline">
    <span class="banner__headline-line">100% West Australian</span>
    <span class="banner__headline-line banner__headline-line--second">Owned &amp; Operated</span>
  </h1>
</div>
</body>
</html>
```